Bref créative
Calvane Chiropractic Stationary/Brochure/Business Card / Post-It Note Design
Calvane Chiropractic Motion and Vitality
Bright & Fun-filled
Marla Teversham, D.C., Diplomate Continental Spinal Council of Athletic Clinicians (w/ "registered' )
417 E Quarry Ln, Suite 83
PO Box 6289
Doylestown PA 18944-0562
Dr.Marla@GoDrMarla.net
www.GoDrMarla.net
* clarification- title should have registered symbol on it
*I would like a Post It Note Design that has
Business Name, Tag Line, Phone Number and " A table is reserved for you and a line to write in appointment time.
* Please include tag line
*I've uploaded both a black background & white background version. I prefer the black background for its pop of color but realized that modifications for letterhead & brochures may be necessary.
the back of the card should have:
Certified Practitioner in the Following:
and then upload logos for
QEL
Pulsetap Systems
KQP / TBVX
VHP
GQLBR
Steelstride Provider

```html
<!DOCTYPE html>
<html lang="en">
<head>
<meta charset="utf-8">
<title>Calvane Chiropractic Stationery Set</title>
<link href="https://fonts.googleapis.com/css2?family=Montserrat:wght@500;700&family=Open+Sans:wght@400;600&display=swap" rel="stylesheet">
<style>
:root{
  --stage-top:#4a4a4a;
  --stage-bottom:#2c2c2c;
  --ink:#151515;
  --paper:#ffffff;
  --paper-soft:#f3f3f3;
  --green:#8cc63f;
  --green-deep:#5f9e1e;
  --purple:#8a3fb8;
  --purple-deep:#5e2288;
  --label:#cfcfcf;
  --faint:#e9efe2;
  --grey-text:#555;
}
*{margin:0;padding:0;box-sizing:border-box}
html,body{width:1200px;height:437px;overflow:hidden}
body{
  background:linear-gradient(180deg,var(--stage-top),var(--stage-bottom));
  font-family:"Open Sans",Arial,sans-serif;
  position:relative;
}
.piece{position:absolute;box-shadow:0 3px 8px rgba(0,0,0,.45);overflow:hidden;background:var(--paper)}
.piece svg.bg{position:absolute;inset:0;width:100%;height:100%}
.label{position:absolute;color:var(--label);font-size:6px;text-align:center}
.brand{position:absolute;display:flex;align-items:center;gap:4px;font-family:"Montserrat",Arial,sans-serif;font-weight:700;text-transform:uppercase;color:var(--green-deep);white-space:nowrap}
.brand .dot{border-radius:50%;background:var(--green);flex:none}
.brand.on-dark{color:var(--paper)}
.tagline{position:absolute;font-family:"Montserrat",Arial,sans-serif;font-weight:500;color:var(--purple);white-space:nowrap}
.contact{position:absolute;color:var(--grey-text);line-height:1.35;white-space:nowrap}
.contact.right{text-align:right}
.contact.on-dark{color:var(--paper)}
.badges{position:absolute;display:grid;grid-template-columns:repeat(3,1fr);gap:5px}
.badge{height:13px;border-radius:2px}
.mark-faint{position:absolute;border-radius:50%;background:var(--faint)}
.footer-text{position:absolute;left:0;right:0;text-align:center;color:var(--grey-text);font-size:3.6px;line-height:1.4}
</style>
</head>
<body>

<!-- Business card front -->
<div class="piece card-front" style="left:24px;top:79px;width:163px;height:96px">
  <svg class="bg" viewBox="0 0 163 96" preserveAspectRatio="none" aria-hidden="true">
    <path d="M0 60 C50 44 110 70 163 52 L163 96 L0 96Z" fill="var(--ink)"/>
    <path d="M0 68 C50 54 110 78 163 62 L163 96 L0 96Z" fill="var(--green)"/>
    <path d="M0 60 C50 44 110 70 163 52" stroke="var(--purple)" stroke-width="1.6" fill="none"/>
  </svg>
  <div class="brand" style="left:8px;top:9px;font-size:6px"><span class="dot" style="width:9px;height:9px"></span>Calvane Chiropractic</div>
  <div class="tagline" style="left:21px;top:19px;font-size:3.8px">Motion and Vitality</div>
  <div class="contact" style="left:8px;top:30px;font-size:3.6px">Marla Teversham, D.C.<br>Diplomate, Continental Spinal Council®</div>
  <div class="contact right on-dark" style="right:8px;top:74px;font-size:3.6px;color:var(--ink)">417 E Quarry Ln, Suite 83 · PO Box 6289<br>Doylestown PA 18944-0562<br>Dr.Marla@GoDrMarla.net · www.GoDrMarla.net</div>
</div>
<div class="label" style="left:24px;top:180px;width:163px">Business Card Front</div>

<!-- Business card back -->
<div class="piece card-back" style="left:24px;top:204px;width:163px;height:98px;background:linear-gradient(180deg,var(--green),var(--green-deep))">
  <svg class="bg" viewBox="0 0 163 98" preserveAspectRatio="none" aria-hidden="true">
    <path d="M0 0 L163 0 L163 14 C110 24 50 8 0 20Z" fill="var(--ink)"/>
    <path d="M0 20 C50 8 110 24 163 14" stroke="var(--purple)" stroke-width="1.4" fill="none"/>
  </svg>
  <div class="contact on-dark" style="left:8px;top:24px;font-size:4px;font-weight:600">Certified Practitioner in the Following:</div>
  <div class="badges" style="left:10px;top:36px;width:143px">
    <span class="badge" style="background:var(--paper)"></span>
    <span class="badge" style="background:var(--paper)"></span>
    <span class="badge" style="background:var(--paper)"></span>
    <span class="badge" style="background:var(--paper)"></span>
    <span class="badge" style="background:var(--paper)"></span>
    <span class="badge" style="background:var(--paper)"></span>
  </div>
  <div class="contact on-dark" style="left:8px;top:80px;font-size:3.4px">QEL · Pulsetap Systems · KQP / TBVX · VHP · GQLBR · Steelstride Provider</div>
</div>
<div class="label" style="left:24px;top:305px;width:163px">Business Card Back</div>

<!-- Post-it note -->
<div class="piece post-it" style="left:24px;top:331px;width:163px;height:89px;background:var(--paper)">
  <div class="contact" style="left:8px;top:8px;font-size:3.8px;font-weight:600">A table is reserved for you</div>
  <div class="badges" style="left:10px;top:22px;width:143px">
    <span class="badge" style="background:var(--purple)"></span>
    <span class="badge" style="background:var(--green)"></span>
    <span class="badge" style="background:var(--ink)"></span>
    <span class="badge" style="background:var(--green)"></span>
    <span class="badge" style="background:var(--purple)"></span>
    <span class="badge" style="background:var(--ink)"></span>
  </div>
  <div class="contact" style="left:8px;top:66px;font-size:3.6px">Appointment time ______________________</div>
</div>
<div class="label" style="left:24px;top:426px;width:163px">Post-It Note Design</div>

<!-- Letterhead option 1 -->
<div class="piece letterhead-one" style="left:223px;top:12px;width:250px;height:401px">
  <svg class="bg" viewBox="0 0 250 401" preserveAspectRatio="none" aria-hidden="true">
    <path d="M0 0 L250 0 L250 30 C170 46 90 14 0 36Z" fill="var(--ink)"/>
    <path d="M0 36 C90 14 170 46 250 30" stroke="var(--purple)" stroke-width="2.5" fill="none"/>
    <path d="M0 41 C90 19 170 51 250 35" stroke="var(--green)" stroke-width="1.2" fill="none"/>
    <path d="M0 382 C80 370 170 392 250 376" stroke="var(--purple)" stroke-width="1.5" fill="none"/>
    <path d="M0 386 C80 374 170 396 250 380" stroke="var(--green)" stroke-width="1" fill="none"/>
  </svg>
  <div class="brand on-dark" style="left:10px;top:7px;font-size:6px"><span class="dot" style="width:11px;height:11px"></span>Calvane Chiropractic</div>
  <div class="contact right on-dark" style="right:12px;top:5px;font-size:3.6px">417 E Quarry Ln, Suite 83<br>Doylestown PA 18944-0562<br>Dr.Marla@GoDrMarla.net</div>
  <div class="mark-faint" style="left:55px;top:140px;width:140px;height:140px"></div>
  <div class="footer-text" style="bottom:6px">www.GoDrMarla.net</div>
</div>
<div class="label" style="left:223px;top:418px;width:250px">Letterhead Option 1</div>

<!-- Letterhead option 2 -->
<div class="piece letterhead-two" style="left:516px;top:12px;width:245px;height:401px">
  <svg class="bg" viewBox="0 0 245 401" preserveAspectRatio="none" aria-hidden="true">
    <path d="M0 378 C80 366 170 390 245 372" stroke="var(--purple)" stroke-width="1.5" fill="none"/>
    <path d="M0 382 C80 370 170 394 245 376" stroke="var(--green)" stroke-width="1" fill="none"/>
  </svg>
  <div class="mark-faint" style="left:52px;top:140px;width:140px;height:140px"></div>
  <div class="footer-text" style="bottom:8px">417 E Quarry Ln, Suite 83 · PO Box 6289 · Doylestown PA 18944-0562<br>Dr.Marla@GoDrMarla.net · www.GoDrMarla.net</div>
</div>
<div class="label" style="left:516px;top:418px;width:245px">Letterhead Option 2</div>

<!-- Envelope green -->
<div class="piece envelope-green" style="left:802px;top:41px;width:386px;height:91px;background:linear-gradient(180deg,var(--green),var(--green-deep))">
  <svg class="bg" viewBox="0 0 386 91" preserveAspectRatio="none" aria-hidden="true">
    <path d="M0 0 L193 52 L386 0" stroke="rgba(255,255,255,.35)" stroke-width="1" fill="none"/>
  </svg>
  <div class="brand on-dark" style="left:160px;top:16px;font-size:5px"><span class="dot" style="width:9px;height:9px;background:var(--paper)"></span>Calvane</div>
</div>

<!-- Envelope purple -->
<div class="piece envelope-purple" style="left:840px;top:106px;width:348px;height:105px;background:linear-gradient(180deg,var(--paper),var(--paper-soft))">
  <svg class="bg" viewBox="0 0 348 105" preserveAspectRatio="none" aria-hidden="true">
    <path d="M0 0 L348 0 L348 22 L174 62 L0 22Z" fill="var(--purple)"/>
    <path d="M0 22 L174 62 L348 22" stroke="var(--purple-deep)" stroke-width="1.2" fill="none"/>
  </svg>
  <div class="brand on-dark" style="left:140px;top:8px;font-size:5px"><span class="dot" style="width:9px;height:9px;background:var(--green)"></span>Calvane</div>
</div>

<!-- Envelope white -->
<div class="piece envelope-white" style="left:802px;top:192px;width:381px;height:106px;background:linear-gradient(180deg,var(--paper),var(--paper-soft))">
  <svg class="bg" viewBox="0 0 381 106" preserveAspectRatio="none" aria-hidden="true">
    <path d="M0 0 L190 60 L381 0" stroke="#d6d6d6" stroke-width="1" fill="none"/>
  </svg>
  <div class="brand" style="left:150px;top:22px;font-size:5px"><span class="dot" style="width:9px;height:9px"></span>Calvane</div>
</div>

<!-- Black card -->
<div class="piece card-dark" style="left:811px;top:283px;width:377px;height:120px;background:var(--ink)">
  <svg class="bg" viewBox="0 0 377 120" preserveAspectRatio="none" aria-hidden="true">
    <path d="M0 70 C120 48 250 84 377 60" stroke="var(--purple)" stroke-width="3" fill="none"/>
    <path d="M0 76 C120 54 250 90 377 66" stroke="var(--green)" stroke-width="1.5" fill="none"/>
  </svg>
  <div class="brand on-dark" style="left:14px;top:14px;font-size:7px"><span class="dot" style="width:13px;height:13px"></span>Calvane Chiropractic</div>
  <div class="tagline" style="left:33px;top:29px;font-size:4.5px;color:var(--green)">Motion and Vitality</div>
  <div class="contact on-dark" style="left:14px;top:90px;font-size:4px">Marla Teversham, D.C. · Dr.Marla@GoDrMarla.net</div>
</div>
<div class="label" style="left:802px;top:409px;width:386px">Envelope Options</div>

</body>
</html>
```